Dog Grooming Provisions - Fur Refresher Spray *

We are Willow Bend Meadows. A city dog's country camp. We are a dog services company providing a camp experience in Upstate NY to the dogs of NYC. We are creating a hand made fur refresher spray for our clients (who are dogs!) for the holidays.
These labels will be used on a 4 ounce vintage style spray bottles. The design should have a vintage grooming provisions feel. We'd like to see the design be a simple, vintage style black with white, charcoal, or very dark almost black green.
The design should incorporate our varying vintage fonts, our logo with "grooming provisions" all natural & handmade, Coat Revive
Obviously this is a gift and while Coat Revive is important, our brand should be a focus. Perhaps a very simple and "elegant" bone but steer away from paws and pet cheesy! Classic, vintage and camp.

Target Market(s)

Upscale Pet Owners of NYC

Industry/Entity Type

Pet Care

Logo Text

Willow Bend Meadows Dog Camp (Dog Camp is is for logo not necessary for label)

Font styles to use
Serif
Sans Serif
Script

Colors
9bcb3b
000000
5c5c5c

Requirements
Must have
• I am looking for a black and white or very simple design. I'd even like our logo for this use be black/white (if possible? - not sure if that can happen?)
• Our branding! Simple vintage feel.
• Grooming Provisions
• Fur Refresher or Coat Revive or Fur Fresh Spray
• Handmade
• All Natural
• Fonts of vintage style - varying with simple and bold (i attached some photos)
Nice to have
• **MAYBE a very Simple Bone (see drawing) - very very thin.
Should not have
• 1. PAWS or cheap looking dog related items
• 2. No bright colors - truly prefer black and white or black with intention to print on plain pulp/brown paper (attached photo)
• 3. Over designed

```html
<!DOCTYPE html>
<html lang="en">
<head>
<meta charset="utf-8">
<title>Coat Revive Label – Willow Bend Meadows</title>
<link href="https://fonts.googleapis.com/css2?family=Staatliches&display=swap" rel="stylesheet">
<style>
  :root {
    --page: #ffffff;
    --label: #111111;
    --ink: #e9e9e9;
    --ink-soft: #bdbdbd;
    --ornament: #8a8a8a;
  }
  html, body {
    margin: 0;
    padding: 0;
    width: 1200px;
    height: 857px;
    overflow: hidden;
    background: var(--page);
  }
  .canvas {
    position: relative;
    width: 1200px;
    height: 857px;
    display: flex;
    align-items: center;
    justify-content: center;
  }
  .label {
    position: relative;
    width: 440px;
    height: 620px;
    background: var(--label);
    box-sizing: border-box;
    padding: 26px 0;
    display: flex;
    flex-direction: column;
    align-items: center;
    font-family: "Staatliches", sans-serif;
    color: var(--ink);
  }
  .label__rule {
    position: absolute;
    left: 0;
    right: 0;
    height: 6px;
    background: var(--ink);
  }
  .label__rule--top { top: 10px; }
  .label__rule--bottom { bottom: 10px; }
  .label__rule::after {
    content: "";
    position: absolute;
    left: 0;
    right: 0;
    height: 0;
    border-top: 1px dashed var(--ink-soft);
  }
  .label__rule--top::after { top: 14px; }
  .label__rule--bottom::after { bottom: 14px; }

  .brand {
    margin-top: 40px;
    display: flex;
    flex-direction: column;
    align-items: center;
    gap: 8px;
  }
  .brand__dot {
    width: 40px;
    height: 40px;
    border-radius: 50%;
    background: var(--ink);
  }
  .brand__name {
    font-size: 24px;
    letter-spacing: 2px;
    color: var(--ink);
  }
  .flourish {
    width: 280px;
    height: 30px;
    margin-top: 22px;
    background: linear-gradient(90deg, transparent, var(--ornament), transparent);
    opacity: .55;
    border-radius: 15px;
  }
  .product-name {
    margin: 14px 0 0;
    font-family: "Staatliches", sans-serif;
    font-weight: 400;
    font-size: 46px;
    line-height: 1.1;
    letter-spacing: 2px;
    color: var(--ink);
  }
  .flourish--low { margin-top: 14px; height: 24px; }

  .provisions {
    margin: 24px 0 0;
    display: flex;
    align-items: center;
    gap: 16px;
    font-size: 22px;
    letter-spacing: 1px;
  }
  .provisions__bone { width: 46px; height: 14px; }
  .dots {
    width: 320px;
    margin-top: 10px;
    border-top: 3px dotted var(--ink-soft);
  }
  .claims {
    margin: 12px 0 0;
    font-size: 22px;
    letter-spacing: 1px;
    display: flex;
    gap: 12px;
    align-items: center;
  }
  .claims__star { font-size: 14px; }
  .established {
    margin: 28px 0 0;
    font-size: 24px;
    letter-spacing: 2px;
  }
</style>
</head>
<body>
  <main class="canvas">
    <article class="label">
      <div class="label__rule label__rule--top"></div>

      <header class="brand">
        <span class="brand__dot"></span>
        <span class="brand__name">Willow Bend Meadows</span>
      </header>

      <div class="flourish" role="img" aria-label="Vintage scroll ornament"></div>

      <h1 class="product-name">Coat Revive</h1>

      <div class="flourish flourish--low" role="img" aria-label="Vintage scroll ornament"></div>

      <p class="provisions">
        <span>Grooming</span>
        <svg class="provisions__bone" viewBox="0 0 46 14" aria-hidden="true">
          <line x1="7" y1="7" x2="39" y2="7" stroke="#e9e9e9" stroke-width="2"/>
          <circle cx="5" cy="4" r="3" fill="#e9e9e9"/>
          <circle cx="5" cy="10" r="3" fill="#e9e9e9"/>
          <circle cx="41" cy="4" r="3" fill="#e9e9e9"/>
          <circle cx="41" cy="10" r="3" fill="#e9e9e9"/>
        </svg>
        <span>Provisions</span>
      </p>

      <div class="dots"></div>

      <p class="claims">
        <span class="claims__star">★</span>
        <span>Handmade</span>
        <span class="claims__star">★</span>
        <span>All Natural</span>
        <span class="claims__star">★</span>
      </p>

      <p class="established">Est 2005</p>

      <div class="label__rule label__rule--bottom"></div>
    </article>
  </main>
</body>
</html>
```